Glasses Promo

I am an optometrist, and we want to get our contact lens buying patients into the habit if buying glasses, too. It's not healthy to be stranded in contact lenses, with no viable glasses options. This post-card sized card would be handed out to all patients that are purchasing contact lenses from the practice, offering a complete pair of glasses, including frames, Vorne lenses, and a one year warranty, starting at $59.
Suggestion for text: buy a year supply of contact lenses and get a complete pair of glasses (new frame, vorne lenses, 1 year warranty) for $59
Updates

Project is now guaranteed / committed.  :) Let's see what you've got!

Target Market(s)

18-40 mixed male / female, quality, 'affordable luxury'

Industry/Entity Type

Promo

Requirements
Must have
• our logo (either one), vorne logo. simple, clean, premium feel.
limit one pair per patient. it should have our address and website. (ideas/info at our website: pennrockoptic.com )
simple, clean, would like a visual reference to glasses, either outline, silhouette, abstract, whatnot. be creative! :)
Nice to have
• frendlio quillo and m+ logos
Should not have
• dinosaurs. although they are awesome.

```html
<!DOCTYPE html>
<html lang="en">
<head>
<meta charset="utf-8">
<title>Glasses Promo Card</title>
<link href="https://fonts.googleapis.com/css2?family=Roboto:wght@300;400;700&family=Roboto+Condensed:wght@700&display=swap" rel="stylesheet">
<style>
  :root {
    --backdrop: #e6e6e6;
    --card: #ffffff;
    --plum: #6b2270;
    --photo-light: #d4d4d4;
    --photo-mid: #9a9a9a;
    --photo-dark: #3a3a3a;
    --text-light: #ffffff;
  }
  * { box-sizing: border-box; margin: 0; padding: 0; }
  html, body {
    width: 1200px;
    height: 750px;
    overflow: hidden;
    background: var(--backdrop);
  }
  .canvas {
    width: 1200px;
    height: 750px;
    display: flex;
    align-items: center;
    justify-content: center;
  }
  .promo-card {
    position: relative;
    width: 500px;
    height: 694px;
    background: var(--card);
    box-shadow: 0 4px 18px rgba(0,0,0,0.18);
  }
  .hero-photo {
    position: absolute;
    left: 20px;
    top: 20px;
    width: 460px;
    height: 310px;
    background:
      radial-gradient(ellipse 38% 55% at 38% 45%, var(--photo-light) 0%, var(--photo-mid) 55%, transparent 80%),
      linear-gradient(100deg, var(--photo-dark) 0%, var(--photo-mid) 45%, var(--photo-light) 100%);
  }
  .brand-tab {
    position: absolute;
    right: 20px;
    top: 20px;
    width: 200px;
    height: 62px;
    background: var(--card);
    border-bottom-left-radius: 26px;
    display: flex;
    align-items: center;
    gap: 10px;
    padding: 0 12px 0 18px;
  }
  .brand-square {
    flex: none;
    width: 30px;
    height: 30px;
    background: var(--plum);
  }
  .brand-name {
    font-family: "Roboto", Arial, sans-serif;
    font-weight: 700;
    font-size: 12px;
    line-height: 1.2;
    letter-spacing: 0.04em;
    text-transform: uppercase;
    color: var(--plum);
  }
  .offer-band {
    position: absolute;
    left: 20px;
    top: 330px;
    width: 460px;
    height: 290px;
    background: var(--plum);
    padding: 28px 30px 0 34px;
    color: var(--text-light);
  }
  .offer-lead {
    font-family: "Roboto", Arial, sans-serif;
    font-weight: 300;
    font-size: 36px;
    line-height: 1.08;
    letter-spacing: -0.01em;
  }
  .offer-deal {
    font-family: "Roboto Condensed", "Arial Narrow", sans-serif;
    font-weight: 700;
    font-size: 36px;
    line-height: 1.08;
    letter-spacing: -0.01em;
  }
  .offer-note {
    position: absolute;
    right: 30px;
    bottom: 44px;
    font-family: "Roboto", Arial, sans-serif;
    font-weight: 300;
    font-size: 13px;
  }
  .offer-limit {
    position: absolute;
    right: 30px;
    bottom: 22px;
    font-family: "Roboto", Arial, sans-serif;
    font-weight: 400;
    font-size: 13px;
  }
  .card-footer {
    position: absolute;
    left: 20px;
    right: 20px;
    bottom: 0;
    height: 74px;
    display: flex;
    align-items: center;
    justify-content: space-between;
    font-family: "Roboto", Arial, sans-serif;
    font-size: 13px;
    color: var(--plum);
  }
  .footer-address { font-weight: 300; }
  .footer-web { font-weight: 700; }
</style>
</head>
<body>
  <main class="canvas">
    <article class="promo-card">
      <div class="hero-photo" role="img" aria-label="Black and white portrait photo of a smiling young woman wearing dark-rimmed glasses"></div>
      <div class="brand-tab">
        <span class="brand-square"></span>
        <span class="brand-name">Pennrock Optic<br>Associates</span>
      </div>
      <section class="offer-band">
        <p class="offer-lead">Buy a year supply of<br>contact lenses and get</p>
        <p class="offer-deal">a complete pair of glasses*<br>for $59.</p>
        <p class="offer-note">* New frame, Vorne lenses and 1 year warranty</p>
        <p class="offer-limit">Limit one pair per patient.</p>
      </section>
      <footer class="card-footer">
        <span class="footer-address">1420 Elm Ridge Road, Pennrock</span>
        <span class="footer-web">pennrockoptic.com</span>
      </footer>
    </article>
  </main>
</body>
</html>
```